Holistic Psychologist needs contemporary business card

I am a psychologist working with adult clients face to face and online. The card needs to work for clients and also referring doctors and medical professionals. It needs to look warm, safe and trustable for clients, but clean and professional enough for doctors. Sometimes I also work in a corporate context.

I am holistic in my approach (mind-body-spirit) so anything conveying connection or integration or wholeness would be good. But again, clean and contemporary please. It can have a little bit of personality.
New logo uploaded.

Probably warm tones and plenty white space to write on one side.

My web pages:
http://lmtherapy.com.au
https://www.facebook.com/MarcellaWhitfordTherapy?ref=hl
Updates

Hi Designers .. I have decided I do need a new logo before finalising a design for the business cards.  I hope to have this available in 4 days from now.

Kindly,

Marcella

New logo now posted, same brief.  Balance of masculine and feminine elements, plenty of white space on one side please.

Keen to see some card designs, thank-you.

Target Market(s)

Audience 1 - Males and females aged 25 years + seeking counselling or coaching. Audience 2 - doctors and health professionals who refer clients.

Industry/Entity Type

Medical

Contact Information for Business Card

Logo

Marcella Whitford
Registered Psychologist

M: 0491 508 243
www.lmtherapy.com.au
marcella@lmtherapy.com.au
Little blue Facebook icon, with "marcella whitford therapy" printed near it.

Font styles to use
Sans Serif

Requirements
Nice to have
• You might want to play with the words "essential you"
Should not have
• Nothing cutesy or too literal

```html
<!DOCTYPE html>
<html lang="en">
<head>
<meta charset="utf-8">
<title>Marcella Whitford – Business Card</title>
<link rel="stylesheet" href="https://fonts.googleapis.com/css2?family=Questrial&family=Crimson+Pro:wght@400&family=Arimo&display=swap">
<style>
  :root {
    --ink: #000000;
    --paper: #ffffff;
    --brand-red: #e2232a;
    --trim-grey: #9a9a9a;
    --social-blue: #3b5998;
  }
  * { margin: 0; padding: 0; box-sizing: border-box; }
  html, body {
    width: 1200px; height: 396px; overflow: hidden; background: var(--paper);
  }
  .canvas { position: relative; width: 1200px; height: 396px; }

  .card {
    position: absolute; top: 27px; width: 557px; height: 344px;
    border: 2px solid var(--ink); background: var(--paper);
  }
  .card--front { left: 37px; }
  .card--back { left: 616px; }
  .card__bleed {
    position: absolute; left: 6px; top: 6px; right: 6px; bottom: 6px;
    border: 2px solid var(--brand-red);
  }
  .card__face {
    position: absolute; left: 19px; top: 19px; width: 517px; height: 304px;
    border: 1px solid var(--trim-grey); overflow: hidden;
  }
  .card__band {
    position: absolute; left: 0; right: 0; bottom: 0; height: 82px;
    background: var(--ink); color: var(--paper);
  }

  .brand {
    position: absolute; display: flex; align-items: center; gap: 12px;
  }
  .brand__dot {
    width: 54px; height: 54px; border-radius: 50%; background: var(--brand-red); flex: none;
  }
  .brand__name {
    color: var(--brand-red); white-space: nowrap; line-height: 1;
  }
  .card--front .brand { left: 108px; top: 156px; }
  .card--front .brand__name {
    font-family: "Questrial", sans-serif; font-size: 29px;
  }
  .card--back .brand { left: 91px; top: 126px; }
  .card--back .brand__dot { width: 52px; height: 52px; }
  .brand__text { display: flex; flex-direction: column; gap: 4px; }
  .card--back .brand__name {
    font-family: "Crimson Pro", serif; font-size: 25px; letter-spacing: 0.5px;
  }
  .brand__role {
    font-family: "Crimson Pro", serif; font-size: 17px; color: var(--ink);
  }

  .website {
    font-family: "Crimson Pro", serif; font-size: 17px;
    text-align: center; padding-top: 19px; letter-spacing: 0.3px;
  }

  .contact { display: flex; align-items: flex-start; height: 100%; padding-top: 17px; }
  .contact__item {
    font-family: "Crimson Pro", serif; font-size: 18px; line-height: 22px; letter-spacing: 0.4px;
  }
  .contact__phone { margin-left: 21px; width: 138px; }
  .contact__divider {
    width: 1px; height: 45px; background: var(--paper); margin-top: 0;
  }
  .contact__email { margin-left: 21px; width: 151px; }
  .contact__social {
    margin-left: 25px; display: flex; gap: 6px;
    font-family: "Arimo", sans-serif; font-size: 14.5px; line-height: 20px;
  }
  .contact__social-mark {
    width: 18px; height: 18px; background: var(--social-blue); margin-top: 1px; flex: none;
  }
</style>
</head>
<body>
<main class="canvas">
  <section class="card card--front" aria-label="Card front">
    <div class="card__bleed"></div>
    <div class="card__face">
      <div class="brand">
        <span class="brand__dot"></span>
        <span class="brand__name">Marcella Whitford</span>
      </div>
      <div class="card__band">
        <p class="website">www.lmtherapy.com.au</p>
      </div>
    </div>
  </section>

  <section class="card card--back" aria-label="Card back">
    <div class="card__bleed"></div>
    <div class="card__face">
      <div class="brand">
        <span class="brand__dot"></span>
        <div class="brand__text">
          <span class="brand__name">Marcella Whitford</span>
          <span class="brand__role">Registered Psychologist</span>
        </div>
      </div>
      <div class="card__band">
        <div class="contact">
          <p class="contact__item contact__phone">0491 508 243</p>
          <span class="contact__divider"></span>
          <p class="contact__item contact__email">marcella@<br>lmtherapy.com.au</p>
          <span class="contact__divider"></span>
          <p class="contact__social">
            <span class="contact__social-mark"></span>
            <span>marcella whitford<br>therapy</span>
          </p>
        </div>
      </div>
    </div>
  </section>
</main>
</body>
</html>
```